A start-up named "trovamind" - a clinical research organization needs a new PowerPoint design

We need a new PowerPoint Design (incl. business card and stationery design) for an early-stage start-up named "trovamind" seeking to build an ecosystem/ strategic partner alliances or consortium of committed and active collaborators to guide important components of the clinical trial.

Our ultimate goal is to avoid false neutrals – therapies that have not been and may never be evaluated in clinical trials due to the costs and/ or complexity.

The final design should highlight our patient-centric approach, innovative study design supported with the novel AI platform to make a stronger impact on patient lives.

Please see the attached brief for more details.
Updates

Requesting the proposals on color-coding, business-card designs, clinical research visuals, and icons as well as stationery design.

Target Market(s)

Pharma/ Biotech Executives
Medical Institutions
Clinical Trial Participants (Patients)

Colors
e34398

Requirements
Must have
• Use the Color Version of purple/ magenta logo

```html
<!DOCTYPE html>
<html lang="en">
<head>
<meta charset="utf-8">
<title>trovamind stationery</title>
<link href="https://fonts.googleapis.com/css2?family=Raleway:wght@400;500;700&family=Roboto:wght@300;400&family=Arimo:ital,wght@0,400;0,700;1,400&display=swap" rel="stylesheet">
<style>
:root{
  --magenta:#e20a84;
  --plum:#b21f62;
  --brand:#c2185b;
  --ink:#111;
  --muted:#444;
  --icon:#8d8d8d;
  --bg:#e2e2e2;
  --paper:#fff;
  --slate:#7f7f7f;
}
*{margin:0;padding:0;box-sizing:border-box}
html,body{width:1024px;height:1200px;overflow:hidden}
body{background:var(--bg);position:relative;font-family:"Arimo",Arial,sans-serif;color:var(--ink)}
.card{position:absolute;width:429px;height:257px;box-shadow:0 8px 24px rgba(0,0,0,.22)}
.card-front{left:63px;top:77px;background:var(--paper)}
.card-back{left:526px;top:75px;background:linear-gradient(90deg,var(--magenta),var(--plum))}
.holder-name{position:absolute;left:35px;top:29px;font-family:"Raleway",sans-serif;font-weight:500;font-size:26px;color:var(--plum);letter-spacing:.3px}
.holder-role{position:absolute;left:35px;top:57px;font-family:"Raleway",sans-serif;font-size:16px;color:var(--muted)}
.contact{position:absolute;left:34px;display:flex;align-items:center;gap:12px;font-family:"Roboto",sans-serif;font-weight:300;font-size:9.5px;line-height:11.5px;color:#333}
.contact svg{width:27px;height:27px;flex:none}
.row-phone{top:112px}.row-mail{top:150px}.row-web{top:189px}
.wordmark{position:absolute;display:flex;align-items:center;font-family:"Raleway",sans-serif;font-weight:700;letter-spacing:-.5px}
.wordmark .mark{display:block;background:currentColor}
.card-front .wordmark{left:225px;top:107px;font-size:31px;color:var(--brand);gap:6px}
.card-front .mark{width:12px;height:12px}
.card-back .wordmark{left:88px;top:100px;font-size:50px;color:#fff;gap:10px}
.card-back .mark{width:18px;height:18px}
.card-band{position:absolute;left:0;bottom:0;width:100%;height:12px;background:linear-gradient(90deg,var(--magenta),var(--plum))}
.letterhead{position:absolute;left:208px;top:397px;width:577px;height:745px;background:var(--paper);box-shadow:0 10px 28px rgba(0,0,0,.2)}
.letterhead .wordmark{left:67px;top:58px;font-size:23px;color:var(--brand);gap:5px}
.letterhead .mark{width:9px;height:9px}
.sender{position:absolute;right:28px;top:45px;text-align:right;font-size:9.6px;line-height:11px;letter-spacing:-.2px}
.edge-tab{position:absolute;right:0;top:33px;width:9px;height:64px;background:var(--magenta)}
.recipient{position:absolute;left:68px;top:153px;font-size:10.4px;line-height:12.2px}
.recipient strong{font-weight:700}
.date{position:absolute;right:67px;top:238px;font-size:10.4px}
.body-copy{position:absolute;left:68px;top:287px;width:442px;font-size:10.4px;line-height:18px;text-align:justify}
.body-copy p+p{margin-top:18px}
.signature{position:absolute;left:68px;top:532px;width:108px;height:26px;background:linear-gradient(90deg,#e8e8e8,#f4f4f4);border-radius:3px}
.signer{position:absolute;left:68px;top:570px;font-size:10.4px;line-height:18px}
.signer strong{font-weight:700}
.footer-band{position:absolute;left:0;top:704px;width:100%;height:25px;background:var(--slate)}
.footer-band .accent{position:absolute;left:0;top:0;width:499px;height:100%;background:var(--magenta)}
.footer-band .site{position:absolute;left:75px;top:8px;font-size:7px;font-weight:700;color:#fff;letter-spacing:.1px}
</style>
</head>
<body>

<section class="card card-front">
  <h1 class="holder-name">MARA ELLISON</h1>
  <p class="holder-role">Solution Manager</p>

  <div class="contact row-phone">
    <svg viewBox="0 0 27 27"><rect width="27" height="27" rx="5" fill="var(--icon)"/><path d="M9 7c1-.6 2 .2 2.6 1.6l.7 1.7c.3.8-.3 1.4-1 2 .8 1.8 2 3 3.6 3.7.6-.7 1.2-1.3 2-1l1.8.8c1.3.6 2 1.5 1.4 2.6-.8 1.4-2.4 2-4 1.4-4-1.5-7.2-4.6-8.6-8.6C7 9.6 7.6 8 9 7z" fill="#fff"/></svg>
    <span>555 . 210 44182007<br>555 . 210 44182007</span>
  </div>
  <div class="contact row-mail">
    <svg viewBox="0 0 27 27"><rect width="27" height="27" rx="5" fill="var(--icon)"/><path d="M13.5 6a5 5 0 0 1 5 5c0 3.6-5 10-5 10s-5-6.4-5-10a5 5 0 0 1 5-5z" fill="#fff"/><circle cx="13.5" cy="11" r="1.8" fill="var(--icon)"/></svg>
    <span>Hello@maraellison.com<br>Email@maraellison.com</span>
  </div>
  <div class="contact row-web">
    <svg viewBox="0 0 27 27"><rect width="27" height="27" rx="5" fill="var(--icon)"/><g fill="none" stroke="#fff" stroke-width="1.1"><circle cx="13.5" cy="13.5" r="7"/><ellipse cx="13.5" cy="13.5" rx="3" ry="7"/><path d="M6.5 13.5h14M7.5 10h12M7.5 17h12"/></g></svg>
    <span>Address here, Suite#1<br>New Avenue, NY -012</span>
  </div>

  <div class="wordmark"><span>trovamind</span><span class="mark"></span></div>
  <div class="card-band"></div>
</section>

<section class="card card-back">
  <div class="wordmark"><span>trovamind</span><span class="mark"></span></div>
</section>

<article class="letterhead">
  <div class="wordmark"><span>trovamind</span><span class="mark"></span></div>
  <address class="sender" style="font-style:normal">Manager<br>Name Of Corporation<br>101 Street Name<br>City, State, 98765</address>
  <div class="edge-tab"></div>

  <address class="recipient" style="font-style:normal">
    <strong>Daniel Reyes</strong><br><em>Manager</em><br>Name Of Corporation<br>101 Street Name<br>City, State, 98765
  </address>

  <p class="date">Date, 01 January, 2021</p>

  <div class="body-copy">
    <p>This is a sample letter that has been placed to demonstrate typing remit (Your Company). Letterhead design. When positioned properly, it will serve to work in harmony with all other elements letterhead. This letterhead design is meant to project an image</p>
    <p>This letterhead design is meant project an image of professionalism reliability. By using simple align we have created a very spacious feeling. The simplicity suggest rengththe spaciousness contributes h aesthetics the layout. These basic qualities along with the (Your Company)</p>
    <p>This letterhead design is based on the (Form of your logo) form (Your Company) logo. Each stationery we have created a very spacious feeling. The simplicity suggests strength the spaciousness contribute part of the (Form of your logo).</p>
  </div>

  <div class="signature" role="img" aria-label="Handwritten signature of Owen Hartley"></div>
  <p class="signer"><strong>Owen Hartley</strong><br>Manager</p>

  <div class="footer-band"><div class="accent"></div><span class="site">WWW.TROVAMIND.COM</span></div>
</article>

</body>
</html>
```